Healthcare patient advocacy company needs banner for conference booth

We need a banner to hang behind us in our booth at conferences. I would like something that prominently features our company name - brovint LLC. And also includes the following language: No employee should face medical debt alone. No Plan should be unrepresented. Expert advocacy and legal support from first bill to final resolution. The colors we use for our other materials are HEX 002C45, FECC73, 00C6CF, E0D5B9, 004C66. And the font is Epilogue. I would welcome some graphics, but no scales of justice or dollar bills or anything like that. I'm attaching some materials so you can see one of our brochures.

Target Market(s)

B2B - health insurers, third-party health care administrators, cost-containment companies

Industry/Entity Type

Healthcare Advocacy

Requirements
Must have
• Name prominently displayed and taglines in project description.
Nice to have
• I would like something easy to read and eye-catching that is not overly complicated or cutsey.
Should not have
• Scales of justice or dollar signs.

```html
<!DOCTYPE html>
<html lang="en">
<head>
<meta charset="utf-8">
<title>brovint LLC — Conference Booth Banner</title>
<link rel="stylesheet" href="https://fonts.googleapis.com/css2?family=Epilogue:wght@400;500;700;800;900&display=swap">
<style>
  :root {
    --navy: #002C45;
    --deep-teal: #004C66;
    --gold: #FECC73;
    --aqua: #00C6CF;
    --sand: #E0D5B9;
    --white: #FFFFFF;
    --backdrop: #E8E8E8;
  }
  * { margin: 0; padding: 0; box-sizing: border-box; }
  html, body {
    width: 1200px;
    height: 2281px;
    overflow: hidden;
    background: var(--backdrop);
    font-family: "Epilogue", sans-serif;
  }
  .banner {
    position: absolute;
    left: 46px;
    top: 587px;
    width: 1108px;
    height: 1108px;
    overflow: hidden;
    background:
      radial-gradient(ellipse 75% 60% at 0% 100%, var(--deep-teal) 0%, rgba(0,76,102,0) 70%),
      var(--navy);
    box-shadow: 0 20px 40px rgba(0,0,0,0.28);
  }
  .banner__pattern {
    position: absolute;
    left: 0;
    top: 0;
    width: 1108px;
    height: 1108px;
  }
  .banner__brand {
    position: absolute;
    left: 60px;
    top: 228px;
    font-size: 74px;
    font-weight: 700;
    letter-spacing: -0.01em;
    color: var(--gold);
    line-height: 1;
  }
  .banner__pill {
    position: absolute;
    left: 59px;
    top: 332px;
    width: 647px;
    height: 78px;
    background: var(--aqua);
    border-radius: 14px 40px 40px 14px;
    color: var(--white);
    font-size: 44px;
    font-weight: 700;
    line-height: 78px;
    padding-left: 33px;
    letter-spacing: -0.01em;
  }
  .banner__headline {
    position: absolute;
    left: 58px;
    top: 430px;
    font-size: 104px;
    font-weight: 800;
    color: var(--white);
    line-height: 1;
    letter-spacing: -0.02em;
  }
  .banner__emphasis {
    position: absolute;
    left: 56px;
    top: 522px;
    font-size: 218px;
    font-weight: 800;
    color: var(--gold);
    line-height: 1;
    letter-spacing: -0.04em;
  }
  .banner__details {
    position: absolute;
    top: 744px;
    left: 58px;
    display: flex;
    font-size: 30px;
    line-height: 39px;
    font-weight: 500;
    color: var(--white);
  }
  .banner__plan { width: 272px; }
  .banner__divider {
    width: 2px;
    height: 108px;
    background: var(--white);
    margin-right: 32px;
  }
  .banner__support { width: 420px; }
  .highlight { color: var(--gold); font-weight: 700; }
  .banner__url {
    position: absolute;
    left: 60px;
    top: 955px;
    font-size: 42px;
    font-weight: 800;
    letter-spacing: 0.28em;
    color: var(--white);
    line-height: 1;
  }
  .banner__url .highlight { font-weight: 800; }
</style>
</head>
<body>
  <section class="banner">
    <svg class="banner__pattern" viewBox="0 0 1108 1108" role="img" aria-label="Geometric pattern of circles and quarter circles in aqua, gold, sand and deep teal framing the top and right edges">
      <defs>
        <linearGradient id="pattern-tone" x1="0" y1="0" x2="1" y2="1">
          <stop offset="0" stop-color="#00C6CF"/>
          <stop offset="0.45" stop-color="#FECC73"/>
          <stop offset="0.75" stop-color="#004C66"/>
          <stop offset="1" stop-color="#00C6CF"/>
        </linearGradient>
      </defs>
      <polygon fill="url(#pattern-tone)" opacity="0.85"
        points="188,0 1108,0 1108,1108 906,1108 906,303 702,303 702,202 385,202 385,101 188,101"/>
    </svg>

    <h1 class="banner__brand">brovint LLC</h1>
    <p class="banner__pill">No employee should face</p>
    <p class="banner__headline">Medical debt</p>
    <p class="banner__emphasis">Alone</p>

    <div class="banner__details">
      <p class="banner__plan">No Plan<br>should be<br><span class="highlight">unrepresented</span></p>
      <span class="banner__divider"></span>
      <p class="banner__support">Expert advocacy and legal<br>support from <span class="highlight">first bill to<br>final resolution</span></p>
    </div>

    <p class="banner__url">www.<span class="highlight">brovinthealth</span>.com</p>
  </section>
</body>
</html>
```